Reseller/Print broker/graphic company needs a website made.

As a print broker specialized in the digital printed textile market I need a website.
Besides digitex I also would like to offer offset printwork.
The products I'm offering are: beachflags, flags, table flags, printed sofa's, banners for in- and outdoor,...
For the offset products I'm offering: brochures, flyers, business cards, envelopes, letterheads,...

Target Market(s)

Printing, digital printing, B2B, offset, graphic design, sign industry

Industry/Entity Type

Digital Printing

Coding

Number of Pages Required

4 page

Font styles to use
Serif
Sans Serif

Colors
33a6d7
00a990
0355a3
9fcc3a

Requirements
Must have
• -On the landing page I would like to show the company, the kind of products we sell and who I am. (Photo with a round phramework, I still don't have a photo)
• -I want to seperate the digitex and offset product pages, and both should have subpages.
• -In the future I would like to implement a webshop.
• - I prefer a white background, and the layout and colors should fit with the company logo.
• -Implement a chatbot, a google map with my address
• - On the bottom of the page I want a URL to the legal info
• -On top of the page all the Social Media icons, see example of the landing page.
• -Use Wordpress, because I'm a bit familiar with this.
• - I have my own hosting and webdomain www.zentrivaprint.eu
• Once the website of finished and online I want to be able to add pages and edit the website.
Nice to have
• -Chatbot
• -Contact form
• -mockup images from offset printwork with the Zentriva Prints name, mockups on flags, beachflags, furniture, in- and outdoor banners
Should not have
• A dark theme

```html
<!DOCTYPE html>
<html lang="en">
<head>
<meta charset="utf-8">
<title>Zentriva Prints — Print Broker</title>
<link href="https://fonts.googleapis.com/css2?family=Montserrat:wght@400;500;600;700&family=Mulish:ital,wght@0,400;0,600;0,700;1,400&display=swap" rel="stylesheet">
<style>
:root{
  --sky:#33a6d7;
  --teal:#00a990;
  --navy:#0355a3;
  --lime:#9fcc3a;
  --ink:#1d1d1d;
  --text:#6b6b6b;
  --line:#d8d8d8;
}
*{box-sizing:border-box;margin:0;padding:0}
html,body{width:1200px;height:3727px;overflow:hidden;background:#fff}
body{font-family:'Mulish',sans-serif;color:var(--text);position:relative}
.abs{position:absolute}
.nw{white-space:nowrap}
h1,h2,h3,.nav,.btn{font-family:'Montserrat',sans-serif}

/* top bar */
.topbar{left:0;top:0;width:1200px;height:45px;background:var(--sky)}
.social{position:absolute;right:20px;top:0;display:flex;height:45px}
.social span{width:50px;height:45px;border-left:1px solid rgba(255,255,255,.35);display:flex;align-items:center;justify-content:center}
.social span i{width:14px;height:14px;border-radius:50%;background:#fff;display:block}

/* header */
.header{left:0;top:45px;width:1200px;height:97px;background:#fff}
.brand{position:absolute;left:120px;top:26px;display:flex;align-items:center;gap:14px}
.brand .mark{width:44px;height:44px;background:var(--teal);border-radius:50%}
.brand .name{font-family:'Montserrat',sans-serif;font-weight:700;font-size:23px;color:var(--navy);line-height:1}
.brand .url{font-size:10px;color:var(--navy);letter-spacing:1px;margin-top:4px}
.nav{position:absolute;right:118px;top:38px;display:flex;gap:34px;font-size:13px;font-weight:600;color:var(--ink)}
.nav .active{color:var(--teal)}

/* hero */
.hero{left:0;top:142px;width:1200px;height:591px;background:linear-gradient(135deg,#b9b2a9 0%,#8e857c 40%,#cfc8bf 70%,#a39c93 100%)}
.hero-title{left:0;top:340px;width:1200px;text-align:center;color:#fff}
.hero-title .l1{font-family:'Montserrat',sans-serif;font-weight:600;font-size:29px;letter-spacing:.5px}
.hero-title .l2{font-family:'Montserrat',sans-serif;font-weight:600;font-size:40px;margin-top:6px}
.arrow{width:26px;height:44px}

/* welcome */
.welcome-title{left:0;top:755px;width:1200px;text-align:center;font-size:30px;font-weight:500;color:var(--ink)}
.welcome-title b{color:var(--teal);font-weight:500}
.welcome-text{left:200px;top:810px;width:800px;text-align:center;font-size:13.5px;line-height:25px}
.feature{width:418px;height:229px;border:1px solid var(--line);border-top:3px solid var(--navy);background:#fff;text-align:center;padding-top:82px}
.feature.alt{border-top-color:var(--teal)}
.feature h3{font-family:'Mulish',sans-serif;font-weight:600;font-size:22px;color:var(--navy);margin-bottom:14px}
.feature.alt h3{color:var(--teal)}
.feature p{font-size:13.5px;line-height:22px;white-space:nowrap}

/* product bands */
.band{left:0;width:1200px;background:linear-gradient(90deg,#e2e2e2,#f5f5f5 30%,#ececec 60%,#f7f7f7)}
.section-h{font-size:24px;font-weight:600;color:var(--sky)}
.section-p{font-size:14px;line-height:24px;color:#555;white-space:nowrap}
.btn{display:inline-block;background:var(--sky);color:#fff;font-size:13px;font-weight:600;border-radius:20px;padding:9px 26px}
.pcard{width:212px;height:262px;background:#fff;box-shadow:0 2px 8px rgba(0,0,0,.12);text-align:center}
.pcard .ph{height:200px}
.pcard p{font-size:15px;color:var(--sky);margin-top:18px}

/* about */
.about{left:0;top:1670px;width:1200px;height:460px;background:linear-gradient(110deg,#0a5db0 0%,#1a7dc8 55%,#3aa4dc 100%)}
.about h2{position:absolute;left:575px;top:80px;font-size:28px;font-weight:600;color:#fff;letter-spacing:.5px}
.about .lead{position:absolute;left:575px;top:130px;font-size:17px;line-height:27px;color:#fff;white-space:nowrap}
.about .body{position:absolute;left:575px;top:205px;font-size:14px;line-height:24px;color:#eaf4fb;white-space:nowrap}
.about .btn{position:absolute;left:575px;top:322px;background:transparent;border:2px solid #fff;padding:9px 26px}

/* testimonials */
.t-title{left:0;top:2612px;width:1200px;text-align:center;font-size:27px;font-weight:600;color:var(--teal);letter-spacing:.5px}
.tcard{width:398px;height:162px;border:1px solid var(--line);background:#fff;text-align:center;padding:48px 20px 0;font-style:italic;font-size:13px;line-height:22px;white-space:nowrap}
.quote{width:44px;height:44px;border-radius:50%;background:var(--teal);color:#fff;font-family:'Montserrat',sans-serif;font-weight:700;font-size:26px;text-align:center;line-height:50px}
.avatar{width:62px;height:62px;border-radius:50%;border:3px solid #fff;box-shadow:0 0 0 1px var(--line)}
.author{font-size:13px;color:#333;text-align:center;width:398px}

/* map */
.map{left:0;top:2961px;width:1200px;height:405px;background:linear-gradient(135deg,#e4e4e4,#d3d3d3 50%,#e9e9e9)}

/* footer */
.footer{left:0;top:3366px;width:1200px;height:361px;background:linear-gradient(100deg,#00a990 0%,#0a8fb0 50%,#0559a6 100%);color:#fff}
.f-brand{position:absolute;left:107px;top:86px;text-align:center;width:200px}
.f-brand .mark{width:50px;height:50px;border-radius:50%;background:#fff;margin:0 auto 14px}
.f-brand .name{font-family:'Montserrat',sans-serif;font-weight:700;font-size:24px;line-height:30px}
.f-brand .url{font-size:10px;letter-spacing:1px;margin-top:6px}
.f-col{position:absolute;top:68px}
.f-col h4{font-family:'Montserrat',sans-serif;font-weight:500;font-size:17px;letter-spacing:.5px;margin-bottom:18px}
.f-col ul{list-style:none;font-size:13px;line-height:26px;padding-left:4px}
.f-rule{position:absolute;left:130px;top:300px;width:940px;height:1px;background:rgba(255,255,255,.35)}
.f-copy{position:absolute;left:0;top:324px;width:1200px;text-align:center;font-size:11px;color:#e6f3f5}
</style>
</head>
<body>

<div class="abs topbar">
  <div class="social"><span><i></i></span><span><i></i></span><span><i></i></span><span><i></i></span><span><i></i></span></div>
</div>

<header class="abs header">
  <div class="brand">
    <div class="mark"></div>
    <div><div class="name">Zentriva Prints</div><div class="url">www.zentrivaprint.eu</div></div>
  </div>
  <nav class="nav"><span class="active">HOME</span><span>ABOUT US</span><span>DIGITEX</span><span>OFFSET</span><span>WHY US</span><span>BLOGS</span><span>CONTACT</span></nav>
</header>

<section class="abs hero" role="img" aria-label="Photo of a designer working at a desktop computer with colour swatches"></section>
<svg class="abs" style="left:0;top:600px" width="1200" height="140" viewBox="0 0 1200 140" aria-hidden="true">
  <path d="M0 40 Q600 150 1200 40 L1200 140 L0 140Z" fill="#fff"/>
</svg>
<div class="abs hero-title"><div class="l1">PRINT BROKER SPECIALISED IN THE</div><div class="l2">DIGITAL PRINTED TEXTILE MARKET</div></div>
<svg class="abs arrow" style="left:94px;top:368px" viewBox="0 0 26 44"><path d="M20 6 L6 22 L20 38" stroke="#fff" stroke-width="4" fill="none"/></svg>
<svg class="abs arrow" style="left:1070px;top:368px" viewBox="0 0 26 44"><path d="M6 6 L20 22 L6 38" stroke="#fff" stroke-width="4" fill="none"/></svg>

<h1 class="abs welcome-title">WELCOME TO <b>ZENTRIVA PRINTS</b></h1>
<p class="abs welcome-text nw">Est eget tempor cursus neque mi consectetuer mi a ultricies massa est sed nisl Class aptent taciti<br>sociosqu ad litora torquent per conubia nostra per inceptos hymenaeos Proin nulla arcu nonummy luctus<br>dictum eget fermentum et lorem Nunc porta convallis pede</p>

<div class="abs feature" style="left:172px;top:956px">
  <h3>Save time &amp; money</h3>
  <p>As a print broker we have the knowledge with choosing<br>the right product from a wide variety of vendors.<br>Have you ever spent hours in comparing all the quote's</p>
</div>
<div class="abs feature alt" style="left:614px;top:956px">
  <h3>Experience and quality</h3>
  <p>Joren is printer with more than 10 years of experience<br>with digital textile printing, offset, silk screen,<br>rotogravure and with print finishing.</p>
</div>
<svg class="abs" style="left:331px;top:912px" width="100" height="108" viewBox="0 0 100 108" aria-hidden="true">
  <polygon points="50,2 96,28 96,80 50,106 4,80 4,28" fill="#fff" stroke="var(--navy)" stroke-width="3"/>
  <polygon points="50,14 86,34 86,74 50,94 14,74 14,34" fill="var(--navy)"/>
  <circle cx="50" cy="54" r="17" fill="none" stroke="#fff" stroke-width="3"/>
  <path d="M50 44 V54 L57 59" stroke="#fff" stroke-width="3" fill="none"/>
</svg>
<svg class="abs" style="left:773px;top:912px" width="100" height="108" viewBox="0 0 100 108" aria-hidden="true">
  <polygon points="50,2 96,28 96,80 50,106 4,80 4,28" fill="#fff" stroke="var(--teal)" stroke-width="3"/>
  <polygon points="50,14 86,34 86,74 50,94 14,74 14,34" fill="var(--teal)"/>
  <circle cx="50" cy="48" r="14" fill="none" stroke="#fff" stroke-width="3"/>
  <path d="M42 60 L38 78 L46 73 L50 80 M58 60 L62 78 L54 73 L50 80" stroke="#fff" stroke-width="3" fill="none"/>
</svg>

<!-- Digitex -->
<section class="abs band" style="top:1230px;height:440px">
  <h2 class="abs section-h" style="left:112px;top:92px">DIGITEX PRODUCT</h2>
  <p class="abs section-p" style="left:112px;top:140px">Maecenas aliquet velit vel turpis<br>Mauris neque metus malesuada<br>nec ultricies sit amet<br>Aorttitor mattis enim in massa<br>libero interdum nec</p>
  <span class="abs btn" style="left:112px;top:284px">VIEW MORE</span>
  <svg class="abs" style="left:352px;top:176px" width="22" height="60" viewBox="0 0 22 60"><path d="M18 4 L4 30 L18 56" stroke="#999" stroke-width="2" fill="none"/></svg>
  <svg class="abs" style="left:1090px;top:176px" width="22" height="60" viewBox="0 0 22 60"><path d="M4 4 L18 30 L4 56" stroke="#999" stroke-width="2" fill="none"/></svg>
  <div class="abs pcard" style="left:397px;top:89px"><div class="ph" role="img" aria-label="Two table flags on a stand" style="background:linear-gradient(135deg,#f4f4f4,#e6dede)"></div><p>Flags</p></div>
  <div class="abs pcard" style="left:633px;top:89px"><div class="ph" role="img" aria-label="Three colourful beach flags" style="background:linear-gradient(135deg,#f7f3e0,#e3eef5)"></div><p>Beachflags</p></div>
  <div class="abs pcard" style="left:869px;top:89px"><div class="ph" role="img" aria-label="Sofa upholstered in printed textile" style="background:linear-gradient(135deg,#c8a38a,#7d6a8e)"></div><p>Printed sofa's</p></div>
</section>

<!-- About -->
<section class="abs about">
  <svg class="abs" style="left:0;top:0" width="1200" height="460" viewBox="0 0 1200 460" aria-hidden="true">
    <path d="M403.5 96 A157 157 0 1 0 482 232 C482 170 500 130 545 118 C500 112 450 90 403.5 96Z" fill="none" stroke="#fff" stroke-width="2"/>
  </svg>
  <div class="abs" role="img" aria-label="Portrait photo of the company owner" style="left:180px;top:87px;width:290px;height:290px;border-radius:50%;border:4px solid #fff;background:linear-gradient(160deg,#e8e6e2,#c9c2ba)"></div>
  <h2>LITTLE ABOUT ME</h2>
  <p class="lead">Maecenas aliquet velit vel turpis Mauris neque metus<br>malesuada nec ultricies sit amet</p>
  <p class="body">massa libero interdum nec interdum vel blandit sed nulla In<br>ullamcorper est eget tempor cursus neque mi consectetuer mi a<br>ultricies massa est sed nisl Class aptent taciti sociosqu ad litora<br>torquent per conubia nostra per inceptos hymenaeos Pr</p>
  <span class="btn">READ MORE</span>
</section>

<!-- Offset -->
<section class="abs band" style="top:2130px;height:441px">
  <svg class="abs" style="left:72px;top:178px" width="22" height="60" viewBox="0 0 22 60"><path d="M18 4 L4 30 L18 56" stroke="#999" stroke-width="2" fill="none"/></svg>
  <svg class="abs" style="left:810px;top:178px" width="22" height="60" viewBox="0 0 22 60"><path d="M4 4 L18 30 L4 56" stroke="#999" stroke-width="2" fill="none"/></svg>
  <div class="abs pcard" style="left:114px;top:90px"><div class="ph" role="img" aria-label="Stack of printed business cards" style="background:linear-gradient(135deg,#f2f2f2,#d9d4cf)"></div><p>Business Cards</p></div>
  <div class="abs pcard" style="left:350px;top:90px"><div class="ph" role="img" aria-label="Colourful printed flyer" style="background:linear-gradient(160deg,#3b2a8a,#c0286e 60%,#f08a2a)"></div><p>Flyers</p></div>
  <div class="abs pcard" style="left:586px;top:90px"><div class="ph" role="img" aria-label="Folded printed brochures" style="background:linear-gradient(135deg,#4a4f57,#2a8fd0 60%,#e6e9ee)"></div><p>Brochures</p></div>
  <h2 class="abs section-h" style="left:835px;top:100px">OFFSET PRODUCTS</h2>
  <p class="abs section-p" style="right:120px;top:146px;text-align:right">Maecenas aliquet velit vel turpis<br>Mauris neque metus malesuada<br>nec ultricies sit amet<br>Aorttitor mattis enim in massa<br>libero interdum nec</p>
  <span class="abs btn" style="left:944px;top:296px">VIEW MORE</span>
</section>

<!-- Testimonials -->
<h2 class="abs t-title">TESTIMONIALS</h2>
<svg class="abs" style="left:132px;top:2742px" width="20" height="36" viewBox="0 0 20 36"><path d="M16 3 L4 18 L16 33" stroke="#888" stroke-width="3" fill="none"/></svg>
<svg class="abs" style="left:1042px;top:2742px" width="20" height="36" viewBox="0 0 20 36"><path d="M4 3 L16 18 L4 33" stroke="#888" stroke-width="3" fill="none"/></svg>
<div class="abs tcard" style="left:181px;top:2678px">Morbi ornare gravida elit Integer congue augue et<br>malesuada iaculis ipsum dui aliquet felis at cursus<br>magna nisl nec elit Praesent elementum</div>
<div class="abs tcard" style="left:616px;top:2678px">Morbi ornare gravida elit Integer congue augue et<br>malesuada iaculis ipsum dui aliquet felis at cursus<br>magna nisl nec elit Praesent elementum</div>
<div class="abs quote" style="left:358px;top:2652px">“</div>
<div class="abs quote" style="left:793px;top:2652px">“</div>
<div class="abs avatar" role="img" aria-label="Client portrait" style="left:349px;top:2801px;background:linear-gradient(160deg,#d9c4b0,#8a7a6a)"></div>
<div class="abs avatar" role="img" aria-label="Client portrait" style="left:784px;top:2801px;background:linear-gradient(160deg,#d6c8bd,#6e6660)"></div>
<p class="abs author" style="left:181px;top:2878px">By Author Name, City Location</p>
<p class="abs author" style="left:616px;top:2878px">By Author Name, City Location</p>

<!-- Map -->
<div class="abs map" role="img" aria-label="Street map showing the company address"></div>

<!-- Footer -->
<footer class="abs footer">
  <div class="f-brand"><div class="mark"></div><div class="name">Zentriva<br>Prints</div><div class="url">www.zentrivaprint.eu</div></div>
  <div class="f-col" style="left:385px"><h4>QUICK LINKS</h4><ul><li>Home</li><li>About Us</li><li>Our Services</li><li>Why Us</li></ul></div>
  <div class="f-col" style="left:589px"><h4>SUBLINKS</h4><ul><li>Offset Product</li><li>Digitex Product</li><li>Testimonials</li><li>Blogs</li></ul></div>
  <div class="f-col" style="left:787px"><h4>RESOURCES</h4><ul><li>Legal Info</li><li>Support</li><li>Contact Us</li></ul></div>
  <svg class="abs" style="left:954px;top:62px" width="104" height="104" viewBox="0 0 104 104" aria-label="Chat assistant">
    <path d="M4 4 H100 V76 H44 L30 98 L28 76 H4Z" fill="none" stroke="#fff" stroke-width="3"/>
    <rect x="34" y="22" width="36" height="30" rx="4" fill="none" stroke="#fff" stroke-width="3"/>
    <circle cx="44" cy="35" r="4" fill="#fff"/><circle cx="60" cy="35" r="4" fill="#fff"/>
    <path d="M44 45 H60" stroke="#fff" stroke-width="3"/>
    <path d="M52 22 V14" stroke="#fff" stroke-width="3"/><circle cx="52" cy="12" r="3" fill="#fff"/>
    <path d="M34 32 H28 V42 H34 M70 32 H76 V42 H70" stroke="#fff" stroke-width="3" fill="none"/>
  </svg>
  <div class="f-rule"></div>
  <p class="f-copy">© 2017 Company Name. All right reserved.</p>
</footer>

</body>
</html>
```